Tatami Hall Sport promotional leaflet to attract new members

We are looking to produce a leaflet for a local judo club to attract seniors and juniors 5+ the leaflet needs to encourage people to attend classes and train in the martial art

Tatami Hall Sport are proud members of the KSB UK (mats for every) and practice traditional judo which mean we wear white Gi's to show cleanliness and tradition.

www.tatamihallsport.co.uk

Target Market(s)

Kids from 5+ and Adults

Font styles to use
Serif

Requirements
Must have
• Must include times of training and how to book onto a beginners induction
• it must look enticing and show that Judo is fun for all
• must highlight we open on Tuesdays and Thursdays
• Juniors are from 6.15pm to 7.15pm
• seniors 7.30pm to 9pm
• classes are held at Vantrel Gym, Unit 7, Marlow Row, Denholm Close, Rustington, West Sussex, BN17 8QT
• We practice on a Sprung floor Mat area and is great for men and women
• first two classes free
Nice to have
• Classes are run by an expeirnced team including
• Dan Merrow 5th Dan and international referee
• Luke Merrow 2nd Dan current Global Grappling Union European Champion

```html
<!DOCTYPE html>
<html lang="en">
<head>
<meta charset="utf-8">
<title>Tatami Hall Sport – Leaflet</title>
<link href="https://fonts.googleapis.com/css2?family=Poppins:ital,wght@0,400;0,500;0,600;0,700;1,500;1,600;1,700&family=Kaushan+Script&display=swap" rel="stylesheet">
<style>
  :root {
    --red: #b3202a;
    --red-dark: #8e1820;
    --ink: #1b1b1b;
    --panel: #2b2b2c;
    --panel-box: #3b3b3d;
    --chevron: #8a8a8c;
    --paper: #ffffff;
    --soft: #c9c9c9;
    --sans: 'Poppins', Arial, sans-serif;
    --script: 'Kaushan Script', cursive;
  }
  * { box-sizing: border-box; margin: 0; padding: 0; }
  html, body { width: 900px; height: 1200px; overflow: hidden; background: var(--paper); }
  .leaflet { position: relative; width: 900px; height: 1200px; overflow: hidden; font-family: var(--sans); color: var(--ink); background: var(--paper); }
  .artwork { position: absolute; inset: 0; }

  .brand { position: absolute; left: 45px; top: 47px; display: flex; align-items: center; gap: 18px; }
  .brand-dot { width: 74px; height: 74px; border-radius: 50%; background: var(--red); }
  .brand-name { font-size: 42px; font-weight: 400; letter-spacing: 1px; color: var(--ink); text-transform: uppercase; }

  .rule { position: absolute; height: 3px; background: #3a3a3a; }
  .rule-top { left: 50px; top: 146px; width: 550px; }
  .rule-bottom { left: 50px; top: 222px; width: 440px; }

  .headline { position: absolute; left: 50px; top: 154px; font-size: 57px; font-weight: 700; color: var(--red); letter-spacing: 0.5px; line-height: 1; }
  .tagline { position: absolute; left: 50px; top: 237px; font-size: 20px; font-weight: 600; line-height: 28px; color: #2a2a2a; }

  .slogan { position: absolute; left: 0; width: 900px; top: 612px; text-align: center; font-family: var(--script); font-size: 72px; color: #d6d6d6; transform: rotate(-3deg); }
  .opening { position: absolute; left: 0; width: 900px; top: 710px; text-align: center; color: #fff; font-size: 29px; font-weight: 600; font-style: italic; }
  .opening u { text-decoration-thickness: 2px; text-underline-offset: 6px; }

  .session { position: absolute; top: 760px; height: 74px; width: 314px; background: var(--panel-box); color: #fff; text-align: center; padding-top: 6px; }
  .session-juniors { left: 65px; }
  .session-seniors { left: 447px; }
  .session-label { font-size: 22px; font-weight: 400; line-height: 26px; }
  .session-time { font-size: 29px; font-weight: 700; line-height: 34px; }

  .facility { position: absolute; left: 0; width: 900px; top: 846px; text-align: center; color: #fff; font-size: 25px; font-weight: 600; font-style: italic; line-height: 30px; }

  .gallery { position: absolute; top: 925px; left: 42px; display: flex; gap: 8px; }
  .gallery-photo { width: 198px; height: 120px; border: 3px solid #5a5a5c; }

  .venue { position: absolute; left: 40px; top: 1083px; color: #fff; }
  .venue-title { font-size: 19px; font-weight: 600; font-style: italic; line-height: 23px; text-transform: uppercase; }
  .venue-address { margin-top: 4px; font-size: 14px; font-weight: 500; line-height: 19px; }

  .team { position: absolute; left: 391px; top: 1091px; color: #fff; }
  .team-intro { font-size: 14.5px; font-weight: 500; text-transform: uppercase; }
  .coaches { display: flex; gap: 14px; margin-top: 8px; }
  .coach { border-left: 2px solid #fff; padding-left: 11px; }
  .coach-name { font-size: 19px; font-weight: 500; text-transform: uppercase; line-height: 22px; }
  .coach-role { font-size: 14px; font-weight: 500; line-height: 19px; }
  .coach-first { width: 207px; }
</style>
</head>
<body>
<main class="leaflet">
  <svg class="artwork" width="900" height="1200" viewBox="0 0 900 1200" xmlns="http://www.w3.org/2000/svg">
    <defs>
      <linearGradient id="gymWarm" x1="0" y1="0" x2="1" y2="1">
        <stop offset="0" stop-color="#c9a56e"/>
        <stop offset="0.5" stop-color="#e6e0d6"/>
        <stop offset="1" stop-color="#9b7a4e"/>
      </linearGradient>
      <linearGradient id="gymBlue" x1="0" y1="0" x2="1" y2="1">
        <stop offset="0" stop-color="#3b4f8a"/>
        <stop offset="0.5" stop-color="#ece9e4"/>
        <stop offset="1" stop-color="#b59a6c"/>
      </linearGradient>
      <linearGradient id="gymMat" x1="0" y1="0" x2="1" y2="1">
        <stop offset="0" stop-color="#caa474"/>
        <stop offset="0.55" stop-color="#eeeae4"/>
        <stop offset="1" stop-color="#c74a4a"/>
      </linearGradient>
      <linearGradient id="giWhite" x1="0" y1="0" x2="1" y2="1">
        <stop offset="0" stop-color="#efeae4"/>
        <stop offset="0.6" stop-color="#d9d2c8"/>
        <stop offset="1" stop-color="#b9b2a8"/>
      </linearGradient>
    </defs>

    <path d="M0 698 L346 553 L900 700 L900 1200 L0 1200 Z" fill="var(--panel)"/>

    <path role="img" aria-label="Judoka in a white gi mid-throw, lifting an opponent off the ground" d="M500 30 C560 10 640 40 700 80 C760 110 790 160 775 240 C770 320 760 400 700 440 C650 460 560 440 540 400 C520 350 470 320 430 300 C410 280 430 270 470 265 C500 230 480 150 470 110 C465 70 470 45 500 30 Z" fill="url(#giWhite)"/>

    <polygon role="img" aria-label="Two juniors practising a grip in the sports hall" points="254,384 433,323 453,483" fill="url(#gymBlue)"/>
    <polygon role="img" aria-label="Junior judokas kneeling in line during class" points="0,553 318,426 428,497 0,698" fill="url(#gymWarm)"/>
    <polygon points="383,544 453,511 453,572" fill="#111"/>
    <polygon role="img" aria-label="Two young children in white gis with red belts" points="482,314 641,337 641,572 482,595" fill="url(#gymBlue)"/>
    <polygon points="636,567 900,675 900,687 636,579" fill="var(--red)"/>
    <polygon role="img" aria-label="Senior members training throws on the mat" points="666,436 900,534 900,675 661,572" fill="url(#gymMat)"/>

    <g transform="translate(28 470) rotate(-27)">
      <polygon points="0,-8 150,-8 168,-30 168,14 150,34 0,34" fill="var(--red)"/>
      <text x="12" y="24" fill="#fff" font-family="Poppins, Arial, sans-serif" font-weight="700" font-size="27">FIRST TWO</text>
      <polygon points="-18,40 150,40 150,80 -18,80 -6,60" fill="var(--red-dark)"/>
      <text x="4" y="72" fill="#fff" font-family="Poppins, Arial, sans-serif" font-weight="600" font-size="14">CLASSES</text>
      <text x="74" y="74" fill="#fff" font-family="Poppins, Arial, sans-serif" font-weight="700" font-size="28">FREE</text>
    </g>

    <g fill="var(--chevron)">
      <polygon points="378,760 402,760 428,797 402,834 378,834 404,797"/>
      <polygon points="412,760 436,760 462,797 436,834 412,834 438,797"/>
      <polygon points="760,760 784,760 810,797 784,834 760,834 786,797"/>
      <polygon points="794,760 818,760 844,797 818,834 794,834 820,797"/>
    </g>

    <polygon points="0,1073 368,1073 328,1200 0,1200" fill="var(--red)"/>
  </svg>

  <div class="brand">
    <span class="brand-dot"></span>
    <span class="brand-name">Tatami Hall Sport</span>
  </div>
  <div class="rule rule-top"></div>
  <h1 class="headline">BECOME THE HERO</h1>
  <div class="rule rule-bottom"></div>
  <p class="tagline">One Of Our Aims Is To Give All Of<br>Our Judokas, The Confidence<br>To Find Their Inner Hero.</p>

  <p class="slogan">Judo is fun for all</p>
  <p class="opening">OPEN ON <u>TUESDAYS</u> AND <u>THURSDAYS</u></p>

  <div class="session session-juniors">
    <div class="session-label">JUNIORS ARE FROM</div>
    <div class="session-time">6.15PM TO 7.15PM</div>
  </div>
  <div class="session session-seniors">
    <div class="session-label">SENIORS ARE FROM</div>
    <div class="session-time">7.30PM TO 9PM</div>
  </div>

  <p class="facility">We practice on a Sprung floor Mat<br>area and is great for men and women</p>

  <div class="gallery">
    <div class="gallery-photo" role="img" aria-label="Two juniors gripping during randori" style="background: linear-gradient(135deg,#b58e5e,#ece8e2 55%,#9a3a3a);"></div>
    <div class="gallery-photo" role="img" aria-label="Instructor standing beside a senior member" style="background: linear-gradient(135deg,#33508c,#ece8e2 55%,#3a4f8f);"></div>
    <div class="gallery-photo" role="img" aria-label="Juniors practising a throw on the mat" style="background: linear-gradient(135deg,#9aa3a0,#ece8e2 50%,#c94848);"></div>
    <div class="gallery-photo" role="img" aria-label="Smiling coach giving a thumbs up" style="background: linear-gradient(135deg,#c4955b,#ece8e2 55%,#a57a4a);"></div>
  </div>

  <div class="venue">
    <p class="venue-title">Classes are held at<br>Vantrel Gym:</p>
    <p class="venue-address">Unit 7, Marlow Row, Denholm Close,<br>Rustington, West Sussex, BN17 8QT</p>
  </div>

  <div class="team">
    <p class="team-intro">Classes are run by an experienced team including:</p>
    <div class="coaches">
      <div class="coach coach-first">
        <p class="coach-name">Dan Merrow</p>
        <p class="coach-role">5th Dan and international<br>referee</p>
      </div>
      <div class="coach">
        <p class="coach-name">Luke Merrow</p>
        <p class="coach-role">2nd Dan current Global Grappling<br>Union European Champion</p>
      </div>
    </div>
  </div>
</main>
</body>
</html>
```